Redesign of Website

We need an overhaul of our website. I've attached our current logo files. Please visit www.pelvorix.com for our current website for information about our company. We are looking for the same type of website (information-based only) so no need for any online store, payments, interactive stuff or anything like that...basically looking for a fresh new look! Also please make sure this design will be mobile-friendly. Thanks!

```html
<!DOCTYPE html>
<html lang="en">
<head>
<meta charset="utf-8">
<title>Pelvorix Consultants, Inc.</title>
<link rel="stylesheet" href="https://fonts.googleapis.com/css2?family=Noto+Serif:wght@400;700&family=Poppins:wght@400;500;600;700&display=swap">
<style>
:root{
  --blue:#0c4a8e;
  --blue-deep:#0a3f7c;
  --green:#9fd196;
  --green-text:#5aab4a;
  --black:#000;
  --white:#fff;
  --ink:#1b1b1b;
}
*{box-sizing:border-box;margin:0;padding:0}
html,body{width:1200px;height:2703px;overflow:hidden}
body{position:relative;background:var(--white);font-family:"Poppins",sans-serif;color:var(--ink)}
.abs{position:absolute}

/* top bar */
.topbar{left:0;top:0;width:1200px;height:45px;background:var(--black);color:var(--white);font-size:12px}
.topbar .item{position:absolute;top:7px;display:flex;align-items:center;gap:8px;white-space:nowrap}
.icon-circle{width:30px;height:30px;border-radius:50%;border:1.5px solid var(--white);display:flex;align-items:center;justify-content:center;flex:none}
.socials{position:absolute;right:162px;top:14px;display:flex;gap:14px}
.socials span{width:16px;height:16px;border-radius:50%;background:var(--white);display:block}

/* header */
.header{left:0;top:45px;width:1200px;height:83px;background:var(--white)}
.brand{position:absolute;left:162px;top:24px;font-family:"Noto Serif",serif;font-weight:700;font-size:30px;color:var(--blue);letter-spacing:.5px}
.nav{position:absolute;left:688px;top:23px;display:flex;align-items:center;gap:22px;font-family:"Noto Serif",serif;font-weight:700;font-size:13px;color:var(--blue)}
.nav a{color:inherit;text-decoration:none;padding:8px 0}
.nav a.active{background:var(--green);border-radius:18px;padding:9px 20px}

/* hero */
.hero{left:0;top:128px;width:1200px;height:638px;background:linear-gradient(180deg,#6b5360 0%,#4a3d4a 25%,#1d1c24 55%,#0c0c10 100%)}
.hero-title{position:absolute;right:164px;top:218px;font-family:"Noto Serif",serif;font-weight:700;font-size:44px;color:var(--white);letter-spacing:.5px;white-space:nowrap}
.hero-sub{position:absolute;right:164px;top:290px;width:600px;text-align:right;font-size:17px;line-height:27px;color:var(--white)}
.hero-btn{position:absolute;left:850px;top:369px;width:188px;height:51px;background:var(--blue);color:var(--white);font-weight:600;font-size:18px;display:flex;align-items:center;justify-content:center;border-radius:2px}
.slides{position:absolute;left:918px;top:584px;display:flex;gap:16px;font-size:12px;color:#ddd}
.slides .on{color:var(--white);font-weight:600;border-bottom:2px solid var(--white)}

/* welcome */
.welcome-photo{left:611px;top:766px;width:589px;height:639px;background:linear-gradient(150deg,#e9eef2 0%,#b8c3cb 40%,#52606b 75%,#2a3540 100%)}
.welcome-strip{left:611px;top:1405px;width:589px;height:13px;background:var(--green)}
.welcome-box{left:0;top:804px;width:611px;height:562px;background:var(--blue);color:var(--white)}
.welcome-box h2{position:absolute;left:162px;top:92px;width:420px;font-family:"Noto Serif",serif;font-weight:400;font-size:38px;line-height:46px;color:var(--green-text)}
.welcome-box h3{position:absolute;left:162px;top:216px;width:400px;font-weight:600;font-size:19px;line-height:27px}
.welcome-box p{position:absolute;left:162px;width:420px;font-size:12px;line-height:21px;color:#e6ecf4}
.btn-green{position:absolute;left:162px;top:472px;width:112px;height:36px;background:var(--green);color:var(--white);font-size:12px;font-weight:600;display:flex;align-items:center;justify-content:center;border-radius:2px}

/* services */
.eyebrow{left:0;top:1513px;width:1200px;text-align:center;font-size:11px;font-weight:700;letter-spacing:3px;color:var(--blue)}
.section-title{left:0;top:1526px;width:1200px;text-align:center;font-family:"Noto Serif",serif;font-weight:400;font-size:38px;color:var(--green-text)}
.cards{left:0;top:1613px;width:1200px;height:299px;display:flex;gap:3px}
.card{flex:1;display:flex;flex-direction:column}
.card .photo{height:225px}
.card .label{height:74px;background:var(--blue);color:var(--white);display:flex;align-items:center;justify-content:center;font-size:14px;font-weight:500;white-space:nowrap}
.card.featured .photo{background:#2a5c98;color:var(--white);font-size:11px;line-height:18px;padding:20px 24px}
.card.featured .photo p{margin-bottom:16px}
.card.featured .label{background:var(--green);color:var(--blue)}
.pager{left:582px;top:1949px;display:flex;gap:6px}
.pager span{width:12px;height:12px;border-radius:50%;border:1.5px solid #999}
.pager .on{border-color:var(--blue);background:radial-gradient(circle,var(--blue) 45%,var(--white) 50%)}

/* contact band */
.contact{left:0;top:2049px;width:1200px;height:339px;background:linear-gradient(180deg,#2a2522 0%,#1a1614 60%,#0e0c0b 100%)}
.contact h2{position:absolute;left:0;top:64px;width:1200px;text-align:center;font-family:"Noto Serif",serif;font-weight:700;font-size:30px;line-height:40px;color:var(--white)}
.contact .item{position:absolute;top:200px;display:flex;align-items:center;gap:20px;color:var(--white);font-size:18px;white-space:nowrap}
.contact .item.phone{font-weight:600}
.big-circle{width:74px;height:74px;border-radius:50%;border:2px solid var(--white);display:flex;align-items:center;justify-content:center;flex:none}

/* newsletter */
.newsletter{left:0;top:2388px;width:1200px;height:90px;background:var(--green)}
.newsletter h2{position:absolute;left:162px;top:20px;font-family:"Noto Serif",serif;font-weight:400;font-size:38px;color:var(--white)}
.newsletter .field{position:absolute;left:517px;top:27px;width:312px;height:36px;background:var(--white);font-size:11px;color:#333;padding:11px 10px}
.newsletter .submit{position:absolute;left:829px;top:27px;width:83px;height:36px;background:var(--blue);color:var(--white);font-size:12px;font-weight:700;display:flex;align-items:center;justify-content:center}

/* footer */
.footer{left:0;top:2478px;width:1200px;height:225px;background:var(--blue);color:var(--white)}
.footer .nav{left:162px;top:51px;color:var(--white);gap:26px;font-size:13px}
.footer .nav a.active{background:var(--green)}
.footer-socials{position:absolute;left:878px;top:52px;display:flex;gap:8px}
.footer-socials span{width:30px;height:30px;border-radius:50%;background:var(--white);display:block}
.footer-socials span.first{background:var(--green)}
.divider{position:absolute;left:162px;top:108px;width:876px;height:1px;background:rgba(255,255,255,.35)}
.finfo{position:absolute;top:133px;display:flex;align-items:center;gap:10px;font-size:12px;line-height:17px;white-space:nowrap}
.finfo .icon-circle{width:38px;height:38px}
.copy{position:absolute;left:836px;top:135px;width:200px;font-size:11px;line-height:20px}
</style>
</head>
<body>

<div class="abs topbar">
  <div class="item" style="left:162px">
    <span class="icon-circle"><svg width="15" height="11" viewBox="0 0 15 11"><rect x="0.5" y="0.5" width="14" height="10" fill="#fff"/><path d="M1 1l6.5 5L14 1" stroke="#000" stroke-width="1.2" fill="none"/></svg></span>
    info@pelvorix.com
  </div>
  <div class="item" style="left:332px;font-weight:600">
    <span class="icon-circle"><svg width="14" height="14" viewBox="0 0 24 24"><path d="M6.6 10.8a15 15 0 006.6 6.6l2.2-2.2c.3-.3.7-.4 1-.2 1.1.4 2.3.6 3.6.6.6 0 1 .4 1 1V20c0 .6-.4 1-1 1A17 17 0 013 4c0-.6.4-1 1-1h3.5c.6 0 1 .4 1 1 0 1.3.2 2.5.6 3.6.1.3 0 .7-.2 1z" fill="#fff"/></svg></span>
    +91-555-014-2276
  </div>
  <div class="socials"><span></span><span></span><span></span><span></span></div>
</div>

<header class="abs header">
  <div class="brand">Pelvorix Consultants</div>
  <nav class="nav"><a class="active">Home</a><a>About us</a><a>Services</a><a>Contact us</a></nav>
</header>

<section class="abs hero" role="img" aria-label="Dusk city skyline with high-rise buildings">
  <h1 class="hero-title">PELVORIX CONSULTANTS, INC.</h1>
  <p class="hero-sub">Pelvorix will give you the essential facts that are critical for solid business decision making and ongoing loan management.</p>
  <div class="hero-btn">CONTACT US</div>
  <div class="slides"><span>01</span><span class="on">02</span><span>03</span></div>
</section>

<div class="abs welcome-photo" role="img" aria-label="Business team meeting around a table in a bright office"></div>
<div class="abs welcome-strip"></div>
<section class="abs welcome-box">
  <h2>Welcome To Pelvorix Consultants</h2>
  <h3>Decades of Experience in Every Phase of Construction</h3>
  <p style="top:285px">Founded in 1990, Pelvorix Consultants prides itself in providing customized, expert services to its clients. Our staff includes professionals who are credentialed and have years of real-world experience.</p>
  <p style="top:384px">We are committed to providing our clients with expert analysis of proposed and ongoing construction projects – providing crucial facts that will lead to lending decisions that end in success.</p>
  <div class="btn-green">READ MORE</div>
</section>

<div class="abs eyebrow">SERVICES</div>
<h2 class="abs section-title">What We Do?</h2>
<div class="abs cards">
  <div class="card">
    <div class="photo" role="img" aria-label="Hands reviewing charts and reports on a desk" style="background:linear-gradient(135deg,#eef2f6,#b9c9da 60%,#7f98b4)"></div>
    <div class="label">01. Property Condition Reports</div>
  </div>
  <div class="card featured">
    <div class="photo">
      <p>-In-depth review of all plans to insure they contain adequate information</p>
      <p>-Analysis of hard costs to determine adequacy of funds</p>
      <p>-Review any missing costs</p>
      <p>-Review of all other related documents</p>
    </div>
    <div class="label">02. Plan &amp; Cost Reviews</div>
  </div>
  <div class="card">
    <div class="photo" role="img" aria-label="Businessman with calculator and banknotes" style="background:linear-gradient(160deg,#3a4452,#6b6f76 55%,#b79a8c)"></div>
    <div class="label">03. Construction Funding Inspections</div>
  </div>
  <div class="card">
    <div class="photo" role="img" aria-label="Small house model on a desk with paperwork" style="background:linear-gradient(150deg,#c9b8a6,#a27e63 55%,#6d4f3c)"></div>
    <div class="label">04. Environmental Transaction Screens</div>
  </div>
</div>
<div class="abs pager"><span class="on"></span><span></span></div>

<section class="abs contact" role="img" aria-label="Support staff with headsets in a call centre">
  <h2>If You Need Any Kind Of Consulting Services<br>Then Fell Free To Contact With Us</h2>
  <div class="item" style="left:318px">
    <span class="big-circle"><svg width="38" height="28" viewBox="0 0 38 28"><rect width="38" height="28" rx="2" fill="#5aab4a"/><path d="M2 3l17 13L36 3M2 26l12-11M36 26L24 15" stroke="#fff" stroke-width="2" fill="none"/></svg></span>
    info@pelvorix.com
  </div>
  <div class="item phone" style="left:612px">
    <span class="big-circle"><svg width="34" height="34" viewBox="0 0 24 24"><path d="M6.6 10.8a15 15 0 006.6 6.6l2.2-2.2c.3-.3.7-.4 1-.2 1.1.4 2.3.6 3.6.6.6 0 1 .4 1 1V20c0 .6-.4 1-1 1A17 17 0 013 4c0-.6.4-1 1-1h3.5c.6 0 1 .4 1 1 0 1.3.2 2.5.6 3.6.1.3 0 .7-.2 1z" fill="#5aab4a"/><path d="M14 3a7 7 0 017 7M14 6.5a3.5 3.5 0 013.5 3.5" stroke="#5aab4a" stroke-width="1.6" fill="none"/></svg></span>
    +91-555-014-2276
  </div>
</section>

<section class="abs newsletter">
  <h2>Newsletter</h2>
  <div class="field">Eamil</div>
  <div class="submit">SUBMIT</div>
</section>

<footer class="abs footer">
  <nav class="nav abs"><a class="active">Home</a><a>About us</a><a>Services</a><a>Contact us</a></nav>
  <div class="footer-socials"><span class="first"></span><span></span><span></span><span></span></div>
  <div class="divider"></div>
  <div class="finfo" style="left:162px">
    <span class="icon-circle"><svg width="18" height="13" viewBox="0 0 15 11"><rect x="0.5" y="0.5" width="14" height="10" fill="#fff"/><path d="M1 1l6.5 5L14 1" stroke="#0c4a8e" stroke-width="1.2" fill="none"/></svg></span>
    info@pelvorix.com
  </div>
  <div class="finfo" style="left:386px;font-weight:600">
    <span class="icon-circle"><svg width="16" height="16" viewBox="0 0 24 24"><path d="M6.6 10.8a15 15 0 006.6 6.6l2.2-2.2c.3-.3.7-.4 1-.2 1.1.4 2.3.6 3.6.6.6 0 1 .4 1 1V20c0 .6-.4 1-1 1A17 17 0 013 4c0-.6.4-1 1-1h3.5c.6 0 1 .4 1 1 0 1.3.2 2.5.6 3.6.1.3 0 .7-.2 1z" fill="#fff"/></svg></span>
    +91-555-014-2276
  </div>
  <div class="finfo" style="left:611px;font-size:10px;line-height:15px">
    <span class="icon-circle"><svg width="14" height="18" viewBox="0 0 14 18"><path d="M7 0a7 7 0 00-7 7c0 5 7 11 7 11s7-6 7-11a7 7 0 00-7-7z" fill="#fff"/><circle cx="7" cy="7" r="2.5" fill="#0c4a8e"/></svg></span>
    <span>48 Harlow Ave, Suite 310<br>Brenton Township, NJ-07018</span>
  </div>
  <div class="copy">©2019 <b>Pelvorix Consultants INC.</b><br>All Right Reserved. | Terms &amp;<br>Conditions.</div>
</footer>

</body>
</html>
```